mediation practice website build

Looking to create a website for new civil mediation practice. Pages would be "home", "about us", "about mediation", "scheduling" (perhaps with some kind of calendar function), "contact us". Would love to be able to update content/text myself.
Target Market(s)
Small to midsize businesses and attorneys representing those size businesses in pending disputes.
Industry/Entity Type
Build
Look and feel
Each slider illustrates characteristics of the customer's brand and the style your logo design should communicate.

```html
<!DOCTYPE html>
<html lang="en">
<head>
<meta charset="utf-8">
<title>Laurelwood Mediation</title>
<link rel="stylesheet" href="https://fonts.googleapis.com/css2?family=Orbitron:wght@600&family=Montserrat:wght@600&family=Open+Sans:wght@400;600&display=swap">
<style>
  :root {
    --slate: #4a5877;
    --navy: #164478;
    --brand: #1b4d8c;
    --nav-bg: #b9b9f7;
    --nav-text: #10106a;
    --nav-active: #03036b;
    --nav-active-text: #c8c8ff;
    --ink: #1d2a1d;
    --heading: #1f311f;
    --month-current: #a6b9f2;
    --rule: #b8bcc4;
    --link-dot: #2c3e2c;
    --base-line: #c4c4c4;
    --white: #ffffff;
  }
  * { box-sizing: border-box; margin: 0; padding: 0; }
  html, body { width: 1200px; height: 885px; overflow: hidden; background: var(--white); }
  .page { position: relative; width: 1200px; height: 885px; font-family: "Open Sans", sans-serif; color: var(--ink); }
  .frame { position: absolute; inset: 0; }
  .brand {
    position: absolute; left: 248px; top: 12px; width: 867px; height: 168px;
    display: flex; align-items: center; justify-content: center;
    font-family: "Open Sans", sans-serif; font-weight: 600; font-size: 46px; color: var(--brand);
  }
  .nav a {
    position: absolute; display: flex; align-items: center; justify-content: center;
    background: var(--nav-bg); color: var(--nav-text); text-decoration: none;
    font-family: "Orbitron", sans-serif; font-weight: 600; font-size: 12px; letter-spacing: 1px; height: 40px;
  }
  .nav a.active { background: var(--nav-active); color: var(--nav-active-text); }
  .rule { position: absolute; left: 248px; top: 223px; width: 867px; height: 2px; background: var(--rule); }
  .text { position: absolute; font-size: 11.3px; line-height: 12px; }
  .text h2 { font-size: 12.3px; font-weight: 600; color: var(--heading); line-height: 12px; }
  .text p { margin-top: 0; }
  .text .gap { margin-top: 12px; }
  .calendar {
    position: absolute; left: 831px; top: 267px; width: 215px; height: 238px;
    background: var(--navy); padding: 8px;
  }
  .calendar ul {
    list-style: none; background: var(--slate); height: 210px; padding: 16px 0 0 21px;
    font-family: "Montserrat", sans-serif; font-weight: 600; font-size: 22.5px; line-height: 28px; color: var(--white);
  }
  .calendar li.current { color: var(--month-current); }
  .links { position: absolute; top: 825px; font-size: 12.3px; font-weight: 600; color: var(--heading); display: flex; align-items: center; gap: 7px; }
  .links::before { content: ""; width: 13px; height: 13px; border-radius: 50%; background: var(--link-dot); }
  .base-line { position: absolute; left: 75px; top: 876px; width: 283px; height: 3px; background: var(--base-line); }
</style>
</head>
<body>
<div class="page">
  <svg class="frame" width="1200" height="885" viewBox="0 0 1200 885" aria-hidden="true">
    <path d="M75 0 H1113 Q1123 0 1123 10 V875 H75 Z" fill="var(--slate)"/>
    <path d="M248 12 H1110 Q1115 12 1115 18 V560 Q1100 790 885 875 H88 V720 Q118 370 248 225 Z" fill="var(--white)"/>
  </svg>

  <header class="brand">Laurelwood Mediation</header>

  <nav class="nav">
    <a href="#" style="left:264px;top:180px;width:96px;">HOME</a>
    <a href="#" style="left:388px;top:181px;width:150px;">ABOUT US</a>
    <a href="#" style="left:569px;top:180px;width:200px;">ABOUT MEDIATION</a>
    <a href="#" class="active" style="left:795px;top:180px;width:150px;">SCHEDULING</a>
    <a href="#" style="left:963px;top:182px;width:150px;">CONTACT US</a>
  </nav>
  <div class="rule"></div>

  <section class="text" style="left:251px;top:259px;width:540px;">
    <h2>This text is used just to show space recommended for Text<br>Welcome to Family Mediation</h2>
    <p class="gap">Family Mediation&nbsp; is an interdisciplinary association of professionals, working together,<br>creating a better way to provide for co-operative conflict resolution relating to families.</p>
    <p class="gap">We help families succeed by providing referrals to Consumers and information to Family<br>Mediators and other like-minded organizations across Canada. Family Mediation in times of<br>conflict can easy, time efficient, inexpensive, dramatically reduce the human and financial<br>cost of conflict resolution. Contact us today for more information.</p>
    <h2 style="margin-top:48px;">Our Vision:</h2>
    <p>Excellence in Family Mediation.</p>
    <h2 style="margin-top:12px;">Our Mission:</h2>
    <p>Family Mediation families, workplaces and communities.organization dedicated to the promotion<br>of mediation nd other forms of conflict resolution for individuals,</p>
  </section>

  <aside class="calendar">
    <ul>
      <li class="current">January 2011</li>
      <li>February 2011</li>
      <li>March 2011</li>
      <li>April 2011</li>
      <li>May 2011</li>
      <li>June 2011</li>
    </ul>
  </aside>

  <section class="text" style="left:248px;top:530px;width:380px;">
    <h2>Mediation's Greatest Attribute...Simplicity</h2>
    <p>&nbsp;"There's no need for a formal setting, no need for a particular<br>no one under oath. All mediation needs is a valid dispute, people<br>interested in resolving the dispute,<br>and a neutral third party to direct these efforts.<br>Mediation is at its most useful and compelling when<br>it is simple, easy, time efficient, inexpensive, and prompt."<br>format, no discovery, no testimony,</p>
  </section>

  <section class="text" style="left:251px;top:651px;width:380px;">
    <h2>Mediation's Greatest Attribute...Simplicity</h2>
    <p>&nbsp;"There's no need for a formal setting, no need for a particular<br>no one under oath. All mediation needs is a valid dispute, people<br>interested in resolving the dispute,<br>and a neutral third party to direct these efforts.<br>Mediation is at its most useful and compelling when<br>it is simple, easy, time efficient, inexpensive, and prompt."<br>format, no discovery, no testimony,</p>
  </section>

  <section class="text" style="left:666px;top:651px;width:380px;">
    <h2>Mediation's Greatest Attribute...Simplicity</h2>
    <p>&nbsp;"There's no need for a formal setting, no need for a particular<br>no one under oath. All mediation needs is a valid dispute, people<br>interested in resolving the dispute,<br>and a neutral third party to direct these efforts.<br>Mediation is at its most useful and compelling when<br>it is simple, easy, time efficient, inexpensive, and prompt."<br>format, no discovery, no testimony,</p>
  </section>

  <div class="links" style="left:255px;">Arbitraiton &amp; Mediation Services</div>
  <div class="links" style="left:621px;">Arbitration &amp; Mediation Services Attorneys</div>
  <div class="base-line"></div>
</div>
</body>
</html>
```